Corporate Company Needs 3-series Flyer Template for Print

Flyer Contest Brief - We need a series of 3 templates to market and communicate our company’s leadership development program, using our corporate design elements. All 3 templates should have similar style, color, and elements --- but be noticeably different.

Template #1 – We need one template to communicate the Program Overview. It will include sections such as: learning objectives, descriptions about the online classes, a summary of required project, and the goals and purpose of the program

Template #2 – We need one template to communicate the details of an “Opening Event”. This template should include sections such as: Event location, event time, flight and hotel recommendations, event agenda, etc.

Template #3 - We need one template to communicate the details of an “Closing/Graduation Event”. This template should include sections such as: Event location, event time, flight and hotel recommendations, event agenda, etc.

Usage: We will edit and use the flyers to communicate our program, update information in the flyer and email the flyer to participants with each new class.

Our corporate design elements: Please refer to the attached PowerPoint file that includes a logo for the program, called KESTREL, and the purple brand color used for the program.

Size: Each template should be 8.5 x 11 inches

Look And Feel: Bold, Modern, Professional

File Type: Because I will edit, I need the flyer to be created in Microsoft Publisher or PowerPoint.

About the Program: The program is called KESTREL. It stands for Keystone Executive Strategy Track for Rising Emerging Leaders. This program is a high profile executive leadership course that lasts for approximately 5 months. Participants attend a live opening event and a live closing / graduation event. Over the course of 5 months the coursework includes: attending online classrooms, regional meetings, e-Learning classes, and manage a project. It is an exclusive program for high profile professional speakers, and it's important for the flyer to be engaging, professional, and clean.

I will need to be able to make small edits back and forth with the successful designer in order to get it just-right. This may only be possibly 2-3 rounds of edits.

Target Market(s)

Professional Executive Leaders in my company. Company is Harbinwell Partners, USA.

Industry/Entity Type

It Company

Colors
6b449b
0792cd
00a990
add136
fbf289
f04a50

Requirements
Must have
• I must be able to edit all elements of the 3 templates. Therefore, it must be in PowerPoint or Publisher. The designs must use our logo and our purple brand color.
Nice to have
• It would be nice if the designer used the colors provided in the PowerPoint file. It would be nice to see icons used creatively.
Should not have
• Design should not have fancy text or use pictures of people.

```html
<!DOCTYPE html>
<html lang="en">
<head>
<meta charset="utf-8">
<title>KESTREL Program Flyers</title>
<link href="https://fonts.googleapis.com/css2?family=Poppins:wght@500&family=Oswald:wght@500&family=Open+Sans:wght@400;600;700&display=swap" rel="stylesheet">
<style>
  :root{
    --purple:#6b449b;
    --purple-deep:#5a2d86;
    --magenta:#e8197c;
    --green:#8dc63f;
    --ink:#2b2b2b;
    --paper:#ffffff;
    --stage:#e7e4df;
  }
  *{box-sizing:border-box;margin:0;padding:0}
  html,body{width:1200px;height:848px;overflow:hidden}
  body{background:var(--stage);font-family:"Open Sans",sans-serif;color:var(--ink);position:relative}

  .flyer{position:absolute;top:55px;width:570px;height:738px;background:var(--paper);box-shadow:0 2px 10px rgba(0,0,0,.18);overflow:hidden}
  .flyer--overview{left:15px}
  .flyer--project{left:615px}

  .brand{position:absolute;left:28px;top:26px}
  .brand__mark{display:flex;align-items:center;gap:8px}
  .brand__square{width:26px;height:26px;background:var(--purple)}
  .brand__name{font-family:"Poppins",sans-serif;font-weight:500;font-size:40px;line-height:1;color:var(--purple);letter-spacing:-.5px}
  .brand__full{font-size:6.4px;font-weight:600;color:var(--purple);margin-top:4px;text-transform:uppercase;letter-spacing:.2px}
  .brand__title{font-family:"Oswald",sans-serif;font-weight:500;font-size:17px;line-height:1.12;color:var(--purple);text-transform:uppercase;margin-top:14px;width:225px}

  .photo{position:absolute}
  .photo--meeting{left:270px;top:0;width:300px;height:228px;background:linear-gradient(160deg,#4a4a52,#a8764a 55%,#6d6f78)}
  .photo--touch{left:0;top:382px;width:262px;height:308px;background:radial-gradient(circle at 40% 45%,#7e9bb8,#2b4a6e 60%,#13233c)}
  .photo--growth{left:270px;top:512px;width:300px;height:178px;background:linear-gradient(135deg,#0a1426,#123a6a 55%,#0b1a30)}
  .photo--chart{left:296px;top:0;width:274px;height:206px;background:linear-gradient(150deg,#0b1730,#17457c 50%,#07101f)}

  .intro{position:absolute;left:0;top:172px;width:262px;height:204px;background:var(--green);color:#fff;padding:14px 16px;font-size:6.6px;line-height:1.32;font-weight:600}
  .intro p+p{margin-top:6px}

  .details{position:absolute;left:282px;top:238px;width:278px;font-size:6.9px;line-height:1.3}
  .details h2{font-size:11px;font-weight:600;color:var(--purple);margin:5px 0 2px}
  .details h2:first-child{margin-top:0}
  .details ul,.details ol{list-style:none}
  .details .sub{margin-left:8px}

  .project{position:absolute;left:0;top:206px;width:570px;height:398px;background:var(--magenta);color:#fff;padding:14px 18px;display:flex;gap:16px;font-size:7.4px;line-height:1.3}
  .project__col{flex:1}
  .project h2{font-size:11px;font-weight:700;margin-bottom:2px}
  .project p{margin-bottom:5px}
  .project ul{list-style:none;margin-bottom:5px}
  .project li{margin-bottom:4px}
  .project strong{font-weight:700}

  .chat{position:absolute;left:0;top:604px;width:570px;height:100px;background:var(--purple-deep);color:#fff;padding:14px 22px}
  .chat h2{font-size:10.5px;font-weight:700;margin-bottom:5px}
  .chat p{font-size:10px;line-height:1.35}
</style>
</head>
<body>

<section class="flyer flyer--overview">
  <header class="brand">
    <div class="brand__mark"><span class="brand__square"></span><span class="brand__name">kestrel</span></div>
    <div class="brand__full">Keystone Executive Strategy Track for Rising Emerging Leaders</div>
    <h1 class="brand__title">Keystone Executive Strategy Track for Rising Emerging Leaders</h1>
  </header>

  <div class="photo photo--meeting" role="img" aria-label="Photo of a team working around a wooden meeting table seen from above"></div>

  <div class="intro">
    <p>KESTREL is a multi-site manager development program designed to build a bench of multi-site managers consistent with the growth of the business and expected rate of labor turnover. Participants in KESTREL have the opportunity to meet, network and collaborate with colleagues representing the spectrum of sectors and business lines in Harbinwell Partners.</p>
    <p>The KESTREL program consists of a live kickoff event, self-directed learning, virtual classes, experiential 'Day in the Life', a project and a closing graduation. The project focus will be on applying knowledge acquired during the program to a real-world business opportunity. The KESTREL participants will track and share the results of their project. Guest speakers from across Harbinwell Partners will present and share experiences and examples during online classes or chats with KESTREL participants.</p>
  </div>

  <div class="photo photo--touch" role="img" aria-label="Photo of a hand touching glowing people icons on a blue screen"></div>

  <div class="details">
    <h2>Online Classes</h2>
    <p>During the program, there are five (5) mandatory MeetWave online classes. More than one scheduled date/time will be available for each topic. KESTREL participants will select the date/time preferred, but must attend all five as a requirement for completing the program.</p>
    <ul>
      <li>Talent Management + Debrief on Adaptive Leadership</li>
      <li>District/Region Finances + Debrief on Leading Across Miles</li>
      <li>Harbinwell Partners Sales Process + Debrief on Lakemont Business Review article, 'Leading From Within'</li>
      <li>Legal and Contracts + Debrief on Lakemont Business Review article, 'Fuel Your Focus, Not Your Calendar'</li>
      <li>Harbinwell Partners Corporate Finance + Debrief on Lakemont Business Review article, 'Whose Task Is It Anyway?'</li>
    </ul>
    <h2>Reading Assignments</h2>
    <p>The following reading assignments must be completed and participants prepared to debrief in discussions held during MeetWave online classes.</p>
    <ol>
      <li>1. Lakemont Business Review articles in LBR's Essential Reads On</li>
    </ol>
    <h2>Self-Leadership:</h2>
    <ul class="sub">
      <li>Leading From Within by Martin L. Greaves</li>
      <li>Whose Task Is It Anyway? by Walter Penrose, Jr. and Dale R. Voss</li>
      <li>Fuel Your Focus, Not Your Calendar by Terry Hollins and Claire Maddox</li>
      <li>What Counts in the Long Run? by Colin M. Fairbanks</li>
    </ul>
    <ol>
      <li>2. The Adaptive Leader by Dr. Paul Harwood</li>
      <li>3. Leading Across Miles by Denise A. Marchetti</li>
    </ol>
  </div>

  <div class="photo photo--growth" role="img" aria-label="Photo of a hand beside a glowing rising arrow graph on dark blue"></div>
</section>

<section class="flyer flyer--project">
  <header class="brand">
    <div class="brand__mark"><span class="brand__square"></span><span class="brand__name">kestrel</span></div>
    <div class="brand__full">Keystone Executive Strategy Track for Rising Emerging Leaders</div>
    <h1 class="brand__title">Keystone Executive Strategy Track for Rising Emerging Leaders</h1>
  </header>

  <div class="photo photo--chart" role="img" aria-label="Photo of a hand pointing at a glowing line chart on a dark blue screen"></div>

  <div class="project">
    <div class="project__col">
      <h2>KESTREL Project</h2>
      <p>Every KESTREL participant will complete a project as one of the requirements for graduation from the program. The RVP or region leader of the KESTREL participant selects an account in the region (not the participant's account) with which the participant will work. In the course of the project, each KESTREL participant will use tools and concepts learned in the program to analyze the operation, identify improvement opportunities, recommend actions and apply leadership skills to work with the district or region leader for the account, account unit leader and unit team to implement, track and measure improvements.</p>
      <p><strong>The KESTREL participant is required to submit work demonstrating the use or completion of the following:</strong></p>
      <ul>
        <li>SWOT analysis on the opportunity account</li>
        <li>Action plan with recommendations, goals and timeline to address identified improvements</li>
        <li>Proforma on the account reflecting the financial impact of proposed actions (including any anticipated costs, and projected financial and other outcomes)</li>
        <li>Present findings in a live meeting to RVP and Region team. Presentation should include: SWOT analysis findings, Recommendations, Proforma projected outcomes for the account and how they will be measured</li>
        <li>Gain RVP agreement on recommended actions to be taken</li>
        <li>Use TraitMap knowledge and adaptive leadership skills to work with the account to implement action items, then track and measure progress and outcomes</li>
        <li>Prepare a QBR/JRC/CBR (quarterly client review) presentation for the account.</li>
      </ul>
      <p>Optional at the discretion of the RVP and RDO/DM: include</p>
    </div>
    <div class="project__col">
      <p>KESTREL participant in the actual QBR/JRC/CBR meeting with the client</p>
      <ul>
        <li>Prepare and present to the RVP and region team a project status update (when participant nears end of KESTREL program) on the opportunity account, including progress on improvements and results achieved so far</li>
      </ul>
      <h2>Day In The Life</h2>
      <p>KESTREL participants must complete four (4) Day in the Life shadowing experiences. Three of the Day in the Life experiences must be conducted with multi-site leaders (e.g. RDO, District Manager, Regional Manager). Of these, one must be a multi-site leader in a different sector from the participant.</p>
      <p>The fourth Day in the Life experience must be with a region or sector level support/corporate department team member. Examples are: sector/division financial director, sector/division marketing manager, sector/division executive chef, sector/division sales director.</p>
      <p>The purpose of the Day in the Life experience is to see the role firsthand, understanding better the role itself and looking for takeaways you may apply to current and future roles in the organization. In Day in the Life experiences with region/sector level support teams, participants should learn how the role supports/interacts with multi-site leaders, expectations and best practices for fostering productive relationships.</p>
      <p>KESTREL participants should keep a list with the names of those shadowed and the date for submission upon request. In addition, the KESTREL program manager will periodically audit DIL by verifying shadow information with the person shadowed and ask the KESTREL participant to provide takeaways from the shadowing experience.</p>
    </div>
  </div>

  <div class="chat">
    <h2>Q+A Chat with KESTREL Graduates</h2>
    <p>We'll host a Chat in LearnHub for KESTREL participants to network online with a KESTREL graduate. KESTREL participants must participate in 2 Q&amp;A Chat sessions during their KESTREL program, but may attend as many Chats as they like. See scheduled dates below and put the dates you prefer on your calendar.</p>
  </div>
</section>

</body>
</html>
```